Uncle Milo's Curdhouse Thank You Postcard

We need a postcard designed to thank some of our top customers from this past holiday season. We are a retail store that offers local and specialty cheese, meat, and jarred goods, as well as homemade chocolates and fudge. We offer customized gift boxes and baskets full of these items. These top customers either purchased large orders for themselves or sent them out as gifts. We would like our thank you post card to have a light background of our grandpa picture and a big thank you across the top in red. We would like the text to say "Thank you for your recent holiday business! Visit our website at www.unclemiloscurdhouse.example to use code THANKU20 at checkout to receive 20% off your purchase through 4/30/16. Thank you again and we look forward to working with you this year!" We would also like our red uncle milos logo on the post card as well, maybe in a bottom corner.

Industry/Entity Type

Store

Font styles to use
Serif
Sans Serif

Requirements
Must have
• Message: "Thank you for your recent holiday business! Visit our website at www.unclemiloscurdhouse.example to use code THANKU20 at checkout to receive 20% off your purchase through 4/30/16. Thank you again and we look forward to working with you this year!"
• Red and gray color. Red uncle milos logo.

```html
<!DOCTYPE html>
<html lang="en">
<head>
<meta charset="utf-8">
<title>Uncle Milo's Curdhouse – Thank You Postcard</title>
<link rel="stylesheet" href="https://fonts.googleapis.com/css2?family=Arimo:ital,wght@0,700;1,700&family=Lora:wght@400;700&display=swap">
<style>
  :root {
    --red: #ee2a1c;
    --outline: #eceef2;
    --ink: #2f3238;
    --photo-light: #dfe1e5;
    --photo-mid: #b9bcc3;
    --photo-dark: #8d9099;
  }
  html, body {
    margin: 0;
    padding: 0;
    width: 1200px;
    height: 924px;
    overflow: hidden;
    background: #ffffff;
  }
  .postcard {
    position: relative;
    width: 1200px;
    height: 924px;
    overflow: hidden;
  }
  .store-photo {
    position: absolute;
    inset: 0;
    background:
      radial-gradient(ellipse at 50% 70%, var(--photo-light) 0%, transparent 55%),
      linear-gradient(100deg, var(--photo-dark) 0%, var(--photo-mid) 14%, var(--photo-light) 30%, var(--photo-mid) 60%, var(--photo-light) 80%, var(--photo-mid) 100%),
      linear-gradient(180deg, var(--photo-light) 0%, var(--photo-mid) 70%, var(--photo-dark) 100%);
    background-blend-mode: normal, multiply;
  }
  .headline {
    position: absolute;
    margin: 0;
    font-family: "Arimo", Arial, sans-serif;
    font-weight: 700;
    font-style: italic;
    font-size: 282px;
    line-height: 1;
    letter-spacing: -10px;
    color: var(--red);
    -webkit-text-stroke: 18px var(--outline);
    paint-order: stroke fill;
    white-space: nowrap;
  }
  .headline-thank { left: 214px; top: 72px; }
  .headline-you { left: 566px; top: 308px; letter-spacing: -22px; }
  .message {
    position: absolute;
    left: 44px;
    top: 590px;
    width: 500px;
    margin: 0;
    font-family: "Lora", Georgia, serif;
    font-size: 22px;
    line-height: 1.45;
    color: var(--ink);
  }
  .message strong { font-weight: 700; }
  .message .code { font-weight: 700; color: var(--red); }
  .brand {
    position: absolute;
    left: 578px;
    top: 676px;
    display: flex;
    align-items: center;
    gap: 18px;
  }
  .brand-mark {
    width: 58px;
    height: 58px;
    background: var(--red);
  }
  .brand-name {
    font-family: "Arimo", Arial, sans-serif;
    font-weight: 700;
    font-size: 44px;
    line-height: 1.1;
    letter-spacing: 2px;
    color: var(--red);
    text-transform: uppercase;
  }
</style>
</head>
<body>
  <main class="postcard">
    <div class="store-photo" role="img" aria-label="Soft grayscale vintage photo of the shop founder in a white coat and bow tie cutting a large wheel of cheese at the store counter"></div>
    <h1 class="headline headline-thank">Thank</h1>
    <div class="headline headline-you" aria-hidden="true">You!</div>
    <p class="message"><strong>Thank you for your recent holiday business!</strong> Visit our website at www.unclemiloscurdhouse.example to use code <span class="code">THANKU20</span> at checkout to receive 20% off your purchase through 4/30/16. Thank you again and we look forward to working with you this year!</p>
    <div class="brand">
      <div class="brand-mark"></div>
      <div class="brand-name">Uncle Milo's<br>Curdhouse</div>
    </div>
  </main>
</body>
</html>
```